Stationery Design Project

KT7 Staffing requires letterhead and business card designs for a company based in London. Just like the name, we're a management resourcing company, providing resources to third party companies. You can see www.kt7staffing-example.com for ideas on existing colour schemes and design concepts that have been implimented and agreed to. Ultimately the design should broadcast professionalism, safety and the concept of growth.

Target Market(s)

Financial institutes; friendly societies (All UK based)

Industry/Entity Type

Safety

Requirements
Must have
• Files produced should be print ready; and the text in them editable (eg address, name etc)

```html
<!DOCTYPE html>
<html lang="en">
<head>
<meta charset="utf-8">
<title>KT7 Staffing Letterhead</title>
<link rel="stylesheet" href="https://fonts.googleapis.com/css2?family=Roboto+Condensed:wght@500&family=Arimo:wght@400&display=swap">
<style>
  :root {
    --canvas: #ffffff;
    --page: #ffffff;
    --page-edge: #8a8a8a;
    --brand-teal: #1f9aa3;
    --brand-sky: #7cc4d6;
    --band-tint: rgba(200, 226, 236, 0.8);
    --band-clear: rgba(200, 226, 236, 0);
    --contact-grey: #8fb4c0;
  }
  * { margin: 0; padding: 0; box-sizing: border-box; }
  html, body {
    width: 1200px;
    height: 900px;
    overflow: hidden;
    background: var(--canvas);
  }
  .letterhead {
    position: absolute;
    left: 282px;
    top: 36px;
    width: 634px;
    height: 824px;
    background: var(--page);
    border: 2px solid var(--page-edge);
  }
  .brand {
    position: absolute;
    left: 22px;
    top: 36px;
    display: flex;
    align-items: center;
    gap: 14px;
  }
  .brand-dot {
    width: 44px;
    height: 44px;
    border-radius: 50%;
    background: var(--brand-sky);
  }
  .brand-name {
    font-family: "Roboto Condensed", Arial, sans-serif;
    font-weight: 500;
    font-size: 44px;
    line-height: 1;
    color: var(--brand-teal);
    letter-spacing: 0.5px;
  }
  .contact-band {
    position: absolute;
    left: 330px;
    top: 40px;
    width: 284px;
    height: 64px;
    border-radius: 4px;
    background: linear-gradient(90deg, var(--band-clear) 0%, var(--band-tint) 45%, var(--band-tint) 100%);
  }
  .contact-phone,
  .contact-address {
    position: absolute;
    font-family: "Arimo", Arial, sans-serif;
    color: var(--contact-grey);
    white-space: nowrap;
    line-height: 1;
  }
  .contact-phone {
    left: 378px;
    top: 50px;
    font-size: 18px;
    letter-spacing: 3px;
    transform: rotate(3deg);
    transform-origin: left center;
  }
  .contact-address {
    left: 402px;
    top: 78px;
    font-size: 14px;
    transform: rotate(8deg);
    transform-origin: left center;
  }
</style>
</head>
<body>
  <main class="letterhead">
    <header class="letterhead-header">
      <div class="brand">
        <span class="brand-dot"></span>
        <span class="brand-name">KT7 Staffing</span>
      </div>
      <div class="contact-band" role="img" aria-label="Soft decorative ribbon behind the contact details"></div>
      <p class="contact-phone">020.555.0148</p>
      <p class="contact-address">14 Ashby Lane, London</p>
    </header>
  </main>
</body>
</html>
```